Business Card Design

We are starting up a new Family run Business mainly offering a Free House Clearance service. We also offer the following chargeable services which include a Removals Service, Delivery and Collection of Items sold or purchased on Bidloft, Swapwren etc, including Motorcycles, Piano's, Furniture, Electrical appliances.
As there are a few Companies offering similar services we need to stand out and show what we do at a glance while appearing Professional and approachable
Updates

TidyNests

i  am liking some of the colours and designs so far but would like to see a few of our services listed as 1 or 2 have already done if this is possible and maybe some emphasis on the FREE House Clearance. thank you 
best regards
derek

Target Market(s)

Commercial and Domestic Tenants and Landlords aswell as Families looking for a friendly sympathetic clearance service after bereavement

Industry/Entity Type

Business

Contact Information for Business Card

TidyNests,
HouseClearance and Removals,
Marlow Dene
LM47 2QT
Tel: 07815239604
Email: enquiries@tidynests-example.info

```html
<!DOCTYPE html>
<html lang="en">
<head>
<meta charset="utf-8">
<title>TidyNests Business Card</title>
<link href="https://fonts.googleapis.com/css2?family=Open+Sans:wght@400;600&display=swap" rel="stylesheet">
<style>
  :root {
    --backdrop: #8a8a8a;
    --card: #ffffff;
    --brand-green: #2f9a3f;
    --band-dark: #2a9a3c;
    --band-light: #bfe6c4;
    --ink: #141414;
  }
  html, body {
    margin: 0;
    width: 1200px;
    height: 901px;
    overflow: hidden;
    background: var(--backdrop);
    font-family: "Open Sans", Arial, sans-serif;
  }
  .stage {
    position: relative;
    width: 1200px;
    height: 901px;
  }
  .card {
    position: absolute;
    width: 540px;
    height: 348px;
    background: var(--card);
    box-shadow: 0 6px 18px rgba(0,0,0,0.25);
    overflow: hidden;
  }
  .card--front { left: 60px; top: 150px; }
  .card--back  { left: 600px; top: 403px; }

  .brand {
    position: absolute;
    left: 40px;
    top: 58px;
    margin: 0;
    font-size: 64px;
    font-weight: 600;
    line-height: 1;
    letter-spacing: -1px;
    color: var(--brand-green);
  }
  .tagline {
    position: absolute;
    left: 42px;
    top: 128px;
    margin: 0;
    font-size: 29px;
    font-weight: 400;
    color: var(--ink);
  }
  .contact {
    position: absolute;
    right: 34px;
    top: 188px;
    margin: 0;
    font-style: normal;
    font-size: 16px;
    line-height: 1.45;
    color: var(--ink);
  }
  .eco-emblem {
    position: absolute;
    left: 30px;
    bottom: 44px;
    width: 76px;
    height: 76px;
    border-radius: 50%;
    background: radial-gradient(circle, #e6efe6 0%, #7cc487 45%, #2f9a3f 100%);
  }
  .band {
    position: absolute;
    left: 0;
    right: 0;
    bottom: 0;
    height: 34px;
    background:
      linear-gradient(to bottom,
        var(--band-dark) 0 3px,
        var(--band-light) 3px 5px,
        var(--band-dark) 5px 8px,
        var(--band-light) 8px 10px,
        var(--band-dark) 10px 13px,
        #e9f6eb 13px 16px,
        var(--band-dark) 16px 100%);
  }
</style>
</head>
<body>
  <main class="stage">
    <section class="card card--front">
      <h1 class="brand">TIDY NESTS</h1>
      <p class="tagline">HouseClearance and Removals.</p>
      <address class="contact">
        Marlow Dene LM47 2QT<br>
        Tel: 07815239604<br>
        Email: enquiries@tidynests-example.info
      </address>
      <div class="eco-emblem" role="img" aria-label="Reduce, reuse, recycle emblem"></div>
      <div class="band"></div>
    </section>

    <section class="card card--back">
      <h2 class="brand">TIDY NESTS</h2>
      <p class="tagline">HouseClearance and Removals.</p>
      <div class="band"></div>
    </section>
  </main>
</body>
</html>
```